Redesign vek7.ch agency website for unique design with speed and conversion

We want to redesign our website vek7.ch. Our omnichannel marketing agency builds webshops and integrates them into existing systems like ERP/CRM and supports with online marketing campaigns like plimtor ads and social media. The target of the redesign is to get a great look and feel for customers to see directly what we do, (please design something for our three focus areas eCommerce, Online marketing and Integration)
and to improve the pages speed drastically for SEO. Please see our attachment.
Target Market(s)
B2B
Industry/Entity Type
eCommerce Agency
Coding
Coded - Design and coding required
Number of Pages Required
5+ page
Look and feel
Each slider illustrates characteristics of the customer's brand and the style your logo design should communicate.

```html
<!DOCTYPE html>
<html lang="en">
<head>
<meta charset="utf-8">
<title>vek7 – Online Marketing Agentur Zürich</title>
<link href="https://fonts.googleapis.com/css2?family=Poppins:wght@400;500;600;700;800&display=swap" rel="stylesheet">
<style>
:root{
  --green:#41d955;
  --green-dark:#2fbf45;
  --ink:#1f1f1f;
  --text:#3d3d3d;
  --muted:#6b6b6b;
  --light:#ececec;
  --footer:#232323;
  --white:#ffffff;
}
*{margin:0;padding:0;box-sizing:border-box}
html,body{width:1200px;height:4366px;overflow:hidden}
body{position:relative;font-family:"Poppins",sans-serif;color:var(--text);background:var(--white)}
.abs{position:absolute}
.photo{position:absolute}
/* hero */
.hero{position:absolute;left:0;top:0;width:1200px;height:755px;background:linear-gradient(100deg,#262626 0%,#3a3a3a 45%,#5b5955 70%,#3b3a38 100%)}
.brand{position:absolute;font-weight:800;color:var(--green);letter-spacing:4px}
.nav{position:absolute;top:42px;left:562px;display:flex;gap:21px;font-size:13px;font-weight:600;color:var(--white)}
.nav .active{color:var(--green)}
.hero h1{position:absolute;left:88px;top:222px;font-size:45px;line-height:57px;font-weight:800;color:var(--white)}
.hero p{position:absolute;left:88px;top:414px;font-size:14.5px;line-height:22px;color:#eee}
.btn{position:absolute;height:46px;border-radius:23px;font-size:13.5px;font-weight:700;display:flex;align-items:center;justify-content:center}
.btn-green{background:var(--green);color:var(--white)}
.btn-white{background:var(--white);color:var(--ink)}
.btn-grey{background:var(--light);color:var(--ink)}
/* services */
.service{position:absolute;top:813px;display:flex;align-items:center;gap:16px;font-size:16.5px;font-weight:700;color:var(--ink)}
.service .ic{width:84px;height:84px;border-radius:50%;background:var(--green);display:flex;align-items:center;justify-content:center}
h2{font-weight:700;color:var(--ink)}
.split h2{position:absolute;font-size:36px;line-height:44px}
.split p{position:absolute;font-size:14.5px;line-height:20.5px;color:var(--text)}
.center{position:absolute;left:0;width:1200px;text-align:center}
.values{position:absolute;left:0;top:2710px;width:1200px;height:358px;background:var(--green)}
.card{position:absolute;top:2875px;width:313px;height:353px}
.card span{position:absolute;left:0;right:0;bottom:28px;text-align:center;font-size:18px;font-weight:700;color:var(--white)}
.partner{position:absolute;top:3820px;font-size:16px;font-weight:600;color:#555;display:flex;align-items:center;gap:8px}
.partner i{display:inline-block;width:16px;height:16px;background:#9a9a9a;border-radius:50%}
.footer{position:absolute;left:0;top:3948px;width:1200px;height:418px;background:var(--footer);color:#ddd}
.footer h3{position:absolute;font-size:20px;font-weight:700;color:var(--white)}
.links{position:absolute;left:422px;top:4072px;list-style:none;font-size:12.5px;line-height:31px}
.links li::before{content:"› ";}
.contact{position:absolute;left:643px;font-size:12.5px;line-height:17px}
.social{position:absolute;top:4118px;width:54px;height:54px;border-radius:50%;background:#393939;color:var(--white);font-size:11px;font-weight:600;display:flex;align-items:center;justify-content:center}
</style>
</head>
<body>

<section class="hero">
  <div class="photo" role="img" aria-label="Business team greeting each other around a laptop in a bright office" style="left:560px;top:150px;width:640px;height:605px;background:radial-gradient(ellipse at 50% 40%,rgba(150,140,130,.55),rgba(40,40,40,0) 70%)"></div>
  <div class="brand" style="left:88px;top:26px;font-size:44px">VEK7</div>
  <nav class="nav"><span class="active">HOME</span><span>ECOMMERCE</span><span>ONLINE MARKETING</span><span>INTEGRATION</span><span>COMPANY ⌄</span></nav>
  <h1>Ihre Online<br>Marketing Agentur<br>in Zürich für KMUs</h1>
  <p>Sie möchten Online die richtigen Menschen erreichen<br>und mehr Umsatz generieren. Kontaktieren Sie uns!</p>
  <div class="btn btn-green" style="left:88px;top:485px;width:138px">OFFERTE</div>
  <div class="btn btn-white" style="left:234px;top:485px;width:136px">TERMIN</div>
</section>

<div class="service" style="left:204px"><div class="ic"><svg width="40" height="40" viewBox="0 0 40 40" fill="none" stroke="#fff" stroke-width="2"><rect x="5" y="7" width="30" height="21" rx="2"/><path d="M14 34h12M20 28v6M13 14h3l2 7h8l2-5H17"/></svg></div>ECOMMERCE</div>
<div class="service" style="left:461px"><div class="ic"><svg width="40" height="40" viewBox="0 0 40 40" fill="none" stroke="#fff" stroke-width="2"><rect x="8" y="12" width="16" height="22" rx="2"/><circle cx="28" cy="10" r="5"/><path d="M12 20h8M12 25h8M26 16v8l6 4"/></svg></div>ONLINE MARKETING</div>
<div class="service" style="left:777px"><div class="ic"><svg width="40" height="40" viewBox="0 0 40 40" fill="none" stroke="#fff" stroke-width="2"><rect x="6" y="6" width="9" height="9"/><rect x="25" y="6" width="9" height="9"/><rect x="6" y="25" width="9" height="9"/><rect x="25" y="25" width="9" height="9"/><path d="M15 10h10M10 15v10M30 15v10M15 30h10"/></svg></div>INTEGRATION</div>

<section class="split">
  <div class="photo" role="img" aria-label="Two colleagues talking at a desk with laptop and coffee" style="left:88px;top:965px;width:491px;height:490px;background:linear-gradient(135deg,#d9d4cc,#a89c8c 55%,#6f6254)"></div>
  <h2 style="left:650px;top:1038px">Your successful entry<br>into Ecommerce</h2>
  <p style="left:650px;top:1147px;width:430px">Do you want to sell your products or services online? But as an SME, don't you have a marketing department with e-commerce know-how? Then you will face a series of questions essential to the success of your web business crucial are:</p>
  <p style="left:650px;top:1264px;width:430px">Which shop system is best suited to your goals? Which online marketing measures really bring you something?</p>
  <div class="btn btn-grey" style="left:650px;top:1350px;width:137px">READ MORE</div>

  <div class="photo" role="img" aria-label="Business people shaking hands in a glass-roofed office" style="left:602px;top:1490px;width:491px;height:490px;background:linear-gradient(160deg,#c3ccd2,#6d7a84 55%,#2f3940)"></div>
  <h2 style="left:129px;top:1563px">Our individual online<br>marketing solutions</h2>
  <p style="left:129px;top:1673px;width:395px">In us you will find a dedicated team with passion, expertise and curiosity for all topics related to e-commerce and online marketing. Our Agency brings you quickly, purposefully and economically with your products online.</p>
  <p style="left:129px;top:1801px;width:395px">Your advantage: We take care of the special field of online marketing for you – you have a free hand for your core competencies and the good...</p>
  <div class="btn btn-grey" style="left:129px;top:1883px;width:137px">READ MORE</div>
</section>

<h2 class="center" style="top:2070px;font-size:36px">Integration</h2>
<p class="center" style="top:2132px;font-size:14px;line-height:20.5px;padding:0 200px">It is a long established fact that a reader will be distracted by the readable content of a page when looking at its layout. The point of using Lorem Ipsum is that it has a more-or-less normal distribution of letters, as opposed to using 'Content here, content here', making it look like readable English.</p>
<div class="photo" role="img" aria-label="Two colleagues looking at a laptop in an office with shelves" style="left:268px;top:2227px;width:665px;height:363px;background:linear-gradient(120deg,#e6e4df,#b9b5ad 50%,#4c5159)"></div>
<svg class="abs" style="left:799px;top:2552px" width="76" height="76" viewBox="0 0 76 76"><circle cx="38" cy="38" r="38" fill="var(--green)"/><path d="M32 28l14 10-14 10z" fill="#fff"/></svg>

<div class="values"></div>
<h2 class="center" style="top:2792px;font-size:36px;color:var(--white)">Company Values</h2>
<div class="card" role="img" aria-label="Man drawing a diagram on a whiteboard" style="left:117px;background:linear-gradient(180deg,#dcdcdc,#9b9b9b 60%,#1e1e1e)"><span>Sustainability</span></div>
<div class="card" role="img" aria-label="Laptop lid with agency branding" style="left:443px;background:linear-gradient(180deg,#4a5460,#1e7c86 55%,#121416)"><span>Quality</span></div>
<div class="card" role="img" aria-label="Smiling man shaking hands with a client" style="left:768px;background:linear-gradient(180deg,#e3e1dc,#a8a39a 60%,#1e1e1e)"><span>Customer orientation</span></div>

<h2 class="center" style="top:3305px;font-size:36px">Customer Feedback</h2>
<div class="abs" aria-hidden="true" style="left:120px;top:3380px;font-size:420px;line-height:1;font-family:Georgia,serif;font-weight:700;color:#e6e6e6">“</div>
<div class="photo" role="img" aria-label="Portrait of the reviewer" style="left:526px;top:3364px;width:148px;height:148px;border-radius:50%;background:linear-gradient(160deg,#e8e8e8,#a9a9a9)"></div>
<div class="center" style="top:3526px;font-size:16px;font-weight:700;color:var(--ink)">MARLENE KOBLER</div>
<div class="center" style="top:3547px;font-size:19px;color:#f2a524;letter-spacing:2px">★★★★★</div>
<p class="center" style="top:3593px;font-size:15px;line-height:24px;padding:0 295px">Wenn Sie Logopädie oder Ergotherapie für sich oder einen Angehörigen benötigen, sind Sie bei uns richtig. Wir verfügen über langjährige Berufserfahrung und hohe Fachkompetenz.</p>
<div class="abs" style="left:88px;top:3730px;width:1024px;height:1px;background:#e2e2e2"></div>

<div class="partner" style="left:90px"><i></i>Plimtor Ads</div>
<div class="partner" style="left:253px;font-size:14px"><i></i>Vantora partners</div>
<div class="partner" style="left:434px"><i></i>Frendly Ads</div>
<div class="partner" style="left:635px;font-size:14px"><i></i>Keystone Partner</div>
<div class="partner" style="left:838px"><i></i>Cartwell</div>
<div class="partner" style="left:1022px"><i></i>Storix</div>

<footer class="footer"></footer>
<div class="brand" style="left:148px;top:4100px;font-size:60px">VEK7</div>
<h3 class="footer-h" style="position:absolute;left:422px;top:4026px;font-size:20px;font-weight:700;color:#fff">Quick links</h3>
<ul class="links" style="color:#ddd"><li>Join Our Team</li><li>Privacy</li><li>Terms of Service</li><li>FAQs</li><li>Affiliates and Partners</li><li>Accessibility</li></ul>
<h3 style="position:absolute;left:643px;top:4026px;font-size:20px;font-weight:700;color:#fff">Contact info</h3>
<svg class="abs" style="left:645px;top:4077px" width="13" height="10" viewBox="0 0 13 10"><rect width="13" height="10" fill="var(--green)"/><path d="M0 0l6.5 5L13 0" stroke="#232323" fill="none"/></svg>
<div class="contact" style="left:666px;top:4074px;color:#ddd">Email:<br>info@vek7.ch</div>
<svg class="abs" style="left:645px;top:4128px" width="13" height="13" viewBox="0 0 24 24"><path fill="var(--green)" d="M6.6 10.8a15 15 0 006.6 6.6l2.2-2.2c.3-.3.7-.4 1-.2 1.1.4 2.3.6 3.6.6.6 0 1 .4 1 1V20c0 .6-.4 1-1 1A17 17 0 013 4c0-.6.4-1 1-1h3.5c.6 0 1 .4 1 1 0 1.3.2 2.5.6 3.6.1.3 0 .7-.2 1z"/></svg>
<div class="contact" style="left:666px;top:4126px;color:#ddd">Phone:<br>+41 44 000 12 34</div>
<svg class="abs" style="left:646px;top:4181px" width="11" height="15" viewBox="0 0 11 15"><path fill="var(--green)" d="M5.5 0A5.5 5.5 0 000 5.5C0 9.6 5.5 15 5.5 15S11 9.6 11 5.5A5.5 5.5 0 005.5 0zm0 7.5a2 2 0 110-4 2 2 0 010 4z"/></svg>
<div class="contact" style="left:666px;top:4179px;color:#ddd">Location:<br>Lindenweg 12, 8004<br>Zurich, Switzerland</div>
<div class="social" style="left:861px">Frendly</div>
<div class="social" style="left:923px">Tweela</div>
<div class="social" style="left:984px">Linkora</div>
<div class="abs" style="left:88px;top:4314px;width:1024px;height:1px;background:#3a3a3a"></div>
<div class="center" style="top:4332px;font-size:12px;color:#ddd">2023 vek7 Marketing GmbH.</div>
<svg class="abs" style="left:1130px;top:4282px" width="42" height="42" viewBox="0 0 42 42"><circle cx="21" cy="21" r="21" fill="var(--green)"/><path d="M21 28V14M15 20l6-6 6 6" stroke="#fff" stroke-width="2" fill="none"/></svg>

</body>
</html>
```